Power Point Digital Signage Template Needed

The North Calloway Health Centre and Pharmacy (ourcalloway.example) needs a power point digital signage template that is customizable and pulls pertinent local information like weather, news and generic health tips. Please use design and colors from art work and website. We would need the power point project to be able to be read clearly at a distance of around 10 - 15 feet and provide the viewer with all information about our clinic/pharmacy services while attracting their attention with local news or weather reports and health tips.

Target Market(s)

People in waiting room, healthcare , family doctor patients to drive pharmacy business and healthcare centre awareness

Industry/Entity Type

Healthcare

Font styles to use
Serif
Sans Serif

Colors

Designer to choose colors to be used in the design.

Requirements
Must have
• Links to real time local weather
• Scrolling News
• Scrolling Health tips
• Fully Customizable
• Power Point Format
• Multiple Slides for each feature (example 1 for real time weather, 1 slide for news, 1 slide for cliinic hours etc)
• At least 20 customizable slides on contiual rotation

```html
<!DOCTYPE html>
<html lang="en">
<head>
<meta charset="UTF-8">
<title>North Calloway Health Centre and Pharmacy – News</title>
<link href="https://fonts.googleapis.com/css2?family=Montserrat:wght@700&family=Roboto:wght@400;500&display=swap" rel="stylesheet">
<style>
  :root {
    --canvas-bg: #ffffff;
    --frame-edge: #3c3c3c;
    --panel-bg: #ecebe7;
    --heading-grey: #8a8a8a;
    --title-dark: #3a3a3a;
    --body-grey: #8c8c8c;
    --brand-teal: #1f9a8a;
  }
  html, body {
    margin: 0;
    padding: 0;
    overflow: hidden;
    background: var(--canvas-bg);
  }
  .slide {
    position: relative;
    width: 1200px;
    height: 675px;
    overflow: hidden;
    background: var(--canvas-bg);
    border-top: 3px solid var(--frame-edge);
    border-right: 3px solid var(--frame-edge);
    box-sizing: border-box;
  }
  .brand {
    position: absolute;
    top: 22px;
    right: 30px;
    display: flex;
    align-items: center;
    gap: 12px;
    font-family: "Roboto", sans-serif;
    font-weight: 500;
    font-size: 18px;
    line-height: 1.2;
    color: var(--brand-teal);
    text-align: right;
  }
  .brand-dot {
    width: 44px;
    height: 44px;
    border-radius: 50%;
    background: var(--brand-teal);
    flex-shrink: 0;
  }
  .slide-heading {
    position: absolute;
    left: 48px;
    top: 152px;
    margin: 0;
    font-family: "Roboto", sans-serif;
    font-weight: 500;
    font-size: 112px;
    line-height: 1;
    letter-spacing: -1px;
    color: var(--heading-grey);
    z-index: 2;
  }
  .news-panel {
    position: absolute;
    left: 0;
    top: 258px;
    width: 1124px;
    height: 417px;
    background: var(--panel-bg);
    padding: 36px 0 0 51px;
    box-sizing: border-box;
  }
  .news-item {
    width: 1000px;
    margin-bottom: 43px;
  }
  .news-title {
    margin: 0 0 6px;
    font-family: "Montserrat", sans-serif;
    font-weight: 700;
    font-size: 37px;
    line-height: 1.2;
    color: var(--title-dark);
  }
  .news-body {
    margin: 0;
    font-family: "Roboto", sans-serif;
    font-weight: 400;
    font-size: 23.5px;
    line-height: 35px;
    color: var(--body-grey);
  }
</style>
</head>
<body>
  <main class="slide">
    <div class="brand">
      <span>North Calloway Health Centre<br>and Pharmacy</span>
      <span class="brand-dot"></span>
    </div>

    <h1 class="slide-heading">NEWS</h1>

    <section class="news-panel">
      <article class="news-item">
        <h2 class="news-title">News Title Here</h2>
        <p class="news-body">Lorem ipsum dolor sir ipsum Lorem ipsum dolor sir ipsum Lorem ipsum dolor sir ipsum Lorem ipsum dolor sir ipsum Lorem ipsum dolor sir ipsum Lorem ipsum dolor sir ipsum Lorem ipsum dolor sir ipsum Lorem ipsum dolor sir ipsum</p>
      </article>
      <article class="news-item">
        <h2 class="news-title">News Title Here</h2>
        <p class="news-body">Lorem ipsum dolor sir ipsum Lorem ipsum dolor sir ipsum Lorem ipsum dolor sir ipsum Lorem ipsum dolor sir ipsum Lorem ipsum dolor sir ipsum Lorem ipsum dolor sir ipsum Lorem ipsum dolor sir ipsum Lorem ipsum dolor sir ipsum</p>
      </article>
    </section>
  </main>
</body>
</html>
```